Criação de Layout para Website para alimenticio
" A Ve Brinola é uma empresa que produz doces finos para eventos (corporativos e sociais), cujo público alvo são consumidores que valorizam um produto de qualidade e diferenciado. "

```html
<!DOCTYPE html>
<html lang="pt-BR">
<head>
<meta charset="utf-8">
<title>Ve Brinola — Doces Finos</title>
<link href="https://fonts.googleapis.com/css2?family=Open+Sans:wght@400;600;700&display=swap" rel="stylesheet">
<style>
:root{
  --brown:#5b5046;
  --brown-dark:#4a4037;
  --mint:#c6e8ec;
  --mint-strong:#b3e0e5;
  --page:#f7f7f7;
  --text:#5a524b;
  --navy:#1a1a3a;
  --footer:#8c9a90;
  --white:#ffffff;
}
*{margin:0;padding:0;box-sizing:border-box}
html,body{width:767px;height:1200px;overflow:hidden;background:var(--page)}
body{position:relative;font-family:'Open Sans',Arial,sans-serif;color:var(--text)}
.abs{position:absolute}

.social{top:52px;left:646px;display:flex;gap:4px}
.social span{width:27px;height:27px;border-radius:50%;background:var(--brown-dark);display:block}
.search{top:85px;left:579px;width:186px;height:19px;background:#e6e6e6;border-radius:2px}
.search-btn{top:85px;left:743px;width:22px;height:19px;background:var(--brown-dark)}

.nav{top:113px;left:2px;width:765px;height:32px;background:var(--brown);border-bottom:2px solid #8a7f75}
.nav a{position:absolute;top:0;height:30px;line-height:30px;color:var(--white);font-weight:700;font-size:13px;text-decoration:none;text-align:center}
.nav .home{left:42px;width:86px;border-right:1px solid #7a6f65}
.nav .quem{left:128px;width:112px;border-right:1px solid #7a6f65}
.nav .produtos{left:571px;width:110px;background:var(--mint);color:var(--brown-dark)}
.nav .contato{left:681px;width:84px}
.burger{position:absolute;left:15px;top:8px;width:18px}
.burger i{display:block;height:3px;background:var(--white);margin-bottom:3px;border-radius:1px}

.brand{top:40px;left:280px;width:220px;height:160px;background:var(--mint);border-radius:18px;display:flex;align-items:center;justify-content:center;z-index:3}
.brand span{font-family:'Open Sans',Arial,sans-serif;font-weight:700;font-size:36px;color:var(--brown)}

.thumb{left:9px;width:233px;height:59px}
.hero{top:152px;left:249px;width:509px;height:318px;background:linear-gradient(180deg,#d7c9c9 0%,#b86a70 45%,#7a2a33 70%,#c9b8b8 100%)}
.caption{top:311px;left:249px;width:509px;height:117px;background:rgba(30,30,30,.72);color:var(--white)}
.caption h2{position:absolute;left:12px;top:6px;font-weight:400;font-size:21px;letter-spacing:-.3px}
.caption p{position:absolute;left:12px;top:44px;width:440px;font-size:10.5px;line-height:17px;color:#e6e6e6}
.caption .more{position:absolute;left:11px;top:82px;width:72px;height:25px;background:var(--mint);color:var(--brown-dark);font-size:10px;font-weight:600;line-height:25px;text-align:center;border-radius:2px}
.dots{position:absolute;right:10px;top:104px;display:flex;gap:5px}
.dots i{width:7px;height:7px;border-radius:50%;border:1px solid var(--white)}
.dots i.on{background:var(--white)}

.rule{top:485px;left:13px;width:744px;height:1px;background:#cfcfcf}
.section-title{top:493px;left:20px;font-size:17.5px;font-weight:700;color:var(--brown);letter-spacing:-.2px}
.feature{top:523px;left:21px;width:215px;height:160px;background:linear-gradient(160deg,#8a8f94,#d9dadb 45%,#c98a3a 70%,#e8e8e8)}
.copy{top:515px;left:248px;width:505px;font-size:13.2px;line-height:15px;color:var(--text)}
.copy p{margin-bottom:7px}
.copy p.gap{margin-bottom:14px}
.copy b{font-weight:700;color:var(--brown)}

.arrow{top:843px;width:28px;height:28px}
.card{top:875px;width:171px;height:125px}
.card-label{top:972px;left:15px;width:171px;height:28px;background:var(--navy);color:var(--white);font-size:8.5px;font-weight:700;line-height:28px;text-align:center;padding-right:6px}
.plus{top:912px;left:92px;color:var(--white);font-size:18px;font-weight:700}
.section-end{top:1018px;left:2px;width:765px;height:1px;background:#d8d8d8}

.footer{top:1034px;left:0;width:767px;height:166px;background:var(--footer);border-top:7px solid var(--mint-strong)}
.col{position:absolute;top:0}
.col h3{font-size:20px;font-weight:700;color:var(--mint-strong);position:absolute;white-space:nowrap}
.col p{font-size:12.5px;line-height:14.5px;color:var(--white);position:absolute;white-space:nowrap}
.btn-mini{position:absolute;height:16px;background:var(--mint);color:var(--brown-dark);font-size:8px;line-height:16px;text-align:center}
.field{position:absolute;height:15px;background:#e8eaec}
</style>
</head>
<body>

<div class="abs social" aria-label="Redes sociais">
  <span></span><span></span><span></span><span></span>
</div>
<div class="abs search"></div>
<div class="abs search-btn">
  <svg width="22" height="19" viewBox="0 0 22 19"><circle cx="10" cy="8.5" r="3" fill="none" stroke="#fff" stroke-width="1.5"/><line x1="12" y1="10.5" x2="15" y2="13.5" stroke="#fff" stroke-width="1.8"/></svg>
</div>

<nav class="abs nav">
  <div class="burger"><i></i><i></i><i></i></div>
  <a class="home">HOME</a>
  <a class="quem">QUEM SOMOS</a>
  <a class="produtos">PRODUTOS</a>
  <a class="contato">CONTATO</a>
</nav>

<div class="abs brand"><span>Ve Brinola</span></div>

<div class="abs thumb" style="top:152px;background:linear-gradient(90deg,#6b3a22,#c99a5a,#f0e8dc,#c99a5a,#6b3a22)" role="img" aria-label="Mesa de festa decorada com bolo e doces"></div>
<div class="abs thumb" style="top:215px;background:linear-gradient(90deg,#5a5f5a,#b9bdb8,#c27fb0,#8e4f86)" role="img" aria-label="Doces decorados em bandeja prateada"></div>
<div class="abs thumb" style="top:280px;background:linear-gradient(90deg,#efeae2,#e39a3c,#f4efe6,#d8c7a8)" role="img" aria-label="Doces finos com frutas laranja"></div>
<div class="abs thumb" style="top:345px;background:linear-gradient(90deg,#8a7a55,#e8a83a,#f0b540,#c88a2a)" role="img" aria-label="Docinhos amarelos em bandeja"></div>
<div class="abs thumb" style="top:411px;background:linear-gradient(90deg,#9cc26a,#eec4b4,#e0528a,#e8c06a,#7a4a3a)" role="img" aria-label="Macarons coloridos"></div>

<div class="abs hero" role="img" aria-label="Docinhos de chocolate com cerejas em bandeja de vidro"></div>
<div class="abs caption">
  <h2>SEJA BEM VINDO !</h2>
  <p>Temos nossa linha fixa, no entanto produzimos doces personalizados para dar um toque exclusivo para o seu evento. Confira nossa linha de produtos.</p>
  <div class="more">SAIBA MAIS</div>
  <div class="dots"><i></i><i class="on"></i><i></i></div>
</div>

<div class="abs rule"></div>
<h1 class="abs section-title">CHÁ DA TARDE / SAZONAIS</h1>
<div class="abs feature" role="img" aria-label="Queijadinhas em prato branco com xícara de café"></div>

<div class="abs copy">
  <p class="gap">Produzimos bolos e doces para tornar aquele chá da tarde ainda mais delicioso!</p>
  <p style="margin-bottom:0"><b>Bolos:</b></p>
  <p class="gap">• <b>Caseiros</b> – Com aroma de infância e gostinho de casa da Vóvó: Laranja, fubá, chocolate, formigueiro, cuca, cenoura com cobertura de chocolate, canela com vinho do Porto, limão, nega maluca, torta de ricota</p>
  <p class="gap">• <b>Chiffon</b> – Bolo leve e muito aerado<br>Sabores: Limão, laranja, maracujá e tangerina</p>
  <p class="gap">• <b>Stolen</b> – Bolo de origem germânica à base de frutas e recheio de marzipan</p>
  <p class="gap">• <b>Pão de mel</b> úmido e com generosa camada de recheio</p>
  <p class="gap">• <b>Brownie</b> belga com ganache</p>
  <p class="gap">• <b>Queijadinhas de leite</b> e toque de canela</p>
  <p class="gap">•&nbsp; <b>Muffins doces e salgados</b></p>
  <p>Confira ainda a nossa linha sazonal ... Não perca os nossos deliciosos ovos de Páscoa! Inove no Natal, dia dos Pais, Mães, Namorados!</p>
</div>

<svg class="abs arrow" style="left:677px" viewBox="0 0 28 28"><circle cx="14" cy="14" r="13" fill="none" stroke="#4a4037" stroke-width="1.5"/><polyline points="16,8 10,14 16,20" fill="none" stroke="#4a4037" stroke-width="2"/></svg>
<svg class="abs arrow" style="left:711px" viewBox="0 0 28 28"><circle cx="14" cy="14" r="13" fill="none" stroke="#4a4037" stroke-width="1.5"/><polyline points="12,8 18,14 12,20" fill="none" stroke="#4a4037" stroke-width="2"/></svg>

<div class="abs card" style="left:15px;background:linear-gradient(180deg,#6a6a6a,#b08a60 50%,#e6e6e6)" role="img" aria-label="Bolo com amêndoas laminadas"></div>
<div class="abs plus">+</div>
<div class="abs card-label">BEM CASADO</div>
<div class="abs card" style="left:200px;background:linear-gradient(180deg,#e8e8e8,#eedcb0 50%,#2f3532)" role="img" aria-label="Bolo chiffon polvilhado com açúcar"></div>
<div class="abs card" style="left:388px;background:linear-gradient(180deg,#f2f2f2,#e8b030 55%,#3a5a8a)" role="img" aria-label="Bolo de maracujá com calda"></div>
<div class="abs card" style="left:575px;background:linear-gradient(160deg,#9a9a9a,#e6d6a8 50%,#b07840)" role="img" aria-label="Stollen fatiado com frutas"></div>

<div class="abs section-end"></div>

<footer class="abs footer">
  <div class="col" style="left:28px">
    <svg style="position:absolute;left:45px;top:25px" width="40" height="38" viewBox="0 0 40 38"><path d="M4 14 Q20 2 36 14 L36 19 L29 19 L29 14 Q20 10 11 14 L11 19 L4 19Z" fill="#c6e8ec"/><path d="M9 20 L31 20 L36 36 L4 36Z" fill="#c6e8ec"/><circle cx="20" cy="28" r="5" fill="#8c9a90"/><circle cx="20" cy="28" r="2.5" fill="#c6e8ec"/></svg>
    <h3 style="left:0;top:66px">Atendimento</h3>
    <p style="left:1px;top:102px">Fone: (11) 98123-4567<br>contato@vebrinola.com.br</p>
  </div>
  <div class="col" style="left:226px">
    <svg style="position:absolute;left:46px;top:22px" width="32" height="44" viewBox="0 0 32 44"><path d="M16 2 C7 2 2 9 2 16 C2 26 16 42 16 42 C16 42 30 26 30 16 C30 9 25 2 16 2Z" fill="#c6e8ec"/><circle cx="16" cy="16" r="6" fill="#8c9a90"/></svg>
    <h3 style="top:66px">Onde Estamos</h3>
    <p style="left:2px;top:96px;font-size:16px">São Paulo</p>
  </div>
  <div class="col" style="left:427px">
    <svg style="position:absolute;left:28px;top:22px" width="44" height="44" viewBox="0 0 44 44"><path d="M4 8 L9 3 L40 36 L41 42 L35 41Z" fill="#c6e8ec"/></svg>
    <h3 style="top:66px">Orçamento</h3>
    <p style="left:1px;top:99px;font-size:11px;line-height:13.5px">Solicite um orçamento<br>sem compromisso.</p>
    <div class="btn-mini" style="left:1px;top:130px;width:62px">SOLICITAR</div>
  </div>
  <div class="col" style="left:590px">
    <svg style="position:absolute;left:36px;top:24px" width="50" height="36" viewBox="0 0 50 36"><rect x="1" y="1" width="48" height="34" rx="3" fill="#c6e8ec"/><polyline points="5,5 25,22 45,5" fill="none" stroke="#8c9a90" stroke-width="3"/><line x1="5" y1="31" x2="19" y2="18" stroke="#8c9a90" stroke-width="3"/><line x1="45" y1="31" x2="31" y2="18" stroke="#8c9a90" stroke-width="3"/></svg>
    <h3 style="top:67px">Newslatter</h3>
    <p style="left:2px;top:100px;font-size:11.5px">Receba nossas novidades</p>
    <svg style="position:absolute;left:0;top:119px" width="13" height="12" viewBox="0 0 13 12"><path d="M1 5 L6.5 1 L12 5 L12 11 L1 11Z" fill="#fff"/><polyline points="1,5 6.5,9 12,5" fill="none" stroke="#8c9a90" stroke-width="1.2"/></svg>
    <div class="field" style="left:16px;top:117px;width:108px"></div>
    <div class="btn-mini" style="left:61px;top:138px;width:62px">CADASTRAR</div>
  </div>
</footer>

</body>
</html>
```